Commercial/Corporate Ashgrove Law needs Website Design

Hi guys. I've started up a new Ashgrove Law and would love your help designing an attractive website. I'll need both design and coding, and to make it easy for us to edit as necessary later, I think it should be built off a Wordpress.org structure.
FIRST IMPRESSIONS
It's very important that the first impression of the website really captures our prospective clients' attention and impresses them. Their first three seconds needs to be good.
I imagine the homepage may be short, with a menu bar and a compelling image, and with a tagline overlaid or underneath (eg. "It's about results.")
The image should be related to our practice areas: eg. IPOs, corporate transactions, or commercial negotiations.
I have previously suggested there could be a skyline image of Sydney or Adelaide. However, because we are based in Adelaide, I don't think Sydney is appropriate - and Adelaide is probably too boring to use.
HOMEPAGE
Being a new firm, we don't have many existing testimonials, and I will be the only lawyer to start with. So we need to focus on the nature of the services we will provide and how my experience can help them. We have an existing logo to use, and I would like the website colour scheme not to clash with that logo (dark blue and white).
After the initial image and tagline there should be a brief introduction to each of the main areas of work, eg. "We specialise in three main areas of practice:"
1. Corporate Transactions and Regulation
2. Business Law and Dispute Resolution
3. Migration Assistance
These should each have an appropriate photo and link to a separate page that briefly describes our services in that area.
Below that there should be a message from me with a photo. Finally, at the bottom, there should be a "Contact Us" section which shows a Google image of our address, contact details, and then our logo with colours inverted.
OTHER PAGES
While we will need some other pages, they should all be fairly simple. I think we will need one page to say "About Us", where I will put information about my experience. I think we will then need one page for each of the 3 areas listed above, which just needs an appropriate image and then text to describe the service. Finally, a "Contact Us" page which I imagine will be the same as the bottom of the homepage.
OTHER DETAILS
For now you can use details from my LinkedIn page to fill out any other text as necessary, or the photo.
Because the logo is square, I would prefer the design of the website also to be rectangular.
Looking forward to seeing your work! Thank you.
Good luck,
Marcus
Target Market(s)
Potential clients:
Businesses with legal issues or disputes
Companies wishing to list on the stock market

```html
<!DOCTYPE html>
<html lang="en">
<head>
<meta charset="utf-8">
<title>Crestmoor Law — Business Law and Dispute Resolution</title>
<link href="https://fonts.googleapis.com/css2?family=Roboto:wght@300;400;500;700;900&display=swap" rel="stylesheet">
<style>
:root{
  --blue:#0a4ea8;
  --blue-deep:#063d88;
  --navy:#1d2433;
  --ink:#222222;
  --muted:#666b73;
  --footer:#1c1c1e;
  --white:#ffffff;
}
*{margin:0;padding:0;box-sizing:border-box}
html,body{width:1200px;height:3529px;overflow:hidden}
body{font-family:'Roboto',sans-serif;color:var(--ink);background:var(--white);position:relative}
.abs{position:absolute}
section,header,nav,footer{position:absolute;left:0;width:1200px;overflow:hidden}

/* header */
.topbar{top:0;height:80px;background:var(--white)}
.brand{left:236px;top:22px;width:140px;text-align:center;font-weight:500;color:var(--navy);line-height:1.15}
.brand-name{font-size:16px;letter-spacing:1px}
.brand-sub{font-size:10px;letter-spacing:5px}
.contact-item{top:22px;display:flex;gap:12px;align-items:center}
.contact-item .big{font-size:15px;color:var(--ink)}
.contact-item .small{font-size:11px;color:var(--blue)}
.socials{left:800px;top:22px;display:flex;gap:10px}
.socials span{width:34px;height:34px;border-radius:50%;background:var(--blue-deep);display:block}

.mainnav{top:80px;height:44px;background:var(--blue)}
.mainnav ul{list-style:none;display:flex;position:absolute;left:250px;top:15px}
.mainnav li{color:#fff;font-size:11.5px;display:flex;align-items:center;white-space:nowrap}
.mainnav li+li::before{content:"";width:4px;height:4px;background:#fff;border-radius:50%;margin:0 9px;opacity:.8}
.mainnav li.current{border-bottom:2px solid #fff;padding-bottom:6px;margin-bottom:-8px}
.search{left:782px;top:8px;width:172px;height:28px;background:var(--blue-deep);color:#c9d7ee;font-size:11px;padding:7px 10px}
.search svg{position:absolute;right:8px;top:7px}

/* hero */
.hero{top:124px;height:461px}
.hero-photo{position:absolute;inset:0;background:linear-gradient(90deg,#2a2e36 0%,#3d424c 45%,#595e66 70%,#353942 100%)}
.hero-frame{left:180px;top:96px;width:210px;height:265px;border:5px solid var(--blue)}
.hero-line{left:110px;top:120px;width:122px;height:2px;background:#fff}
.hero-text{left:250px;top:140px;color:#fff}
.hero-text .l1{font-size:30px;font-weight:300;letter-spacing:.5px}
.hero-text .l2{font-size:56px;font-weight:700;line-height:1.05;margin-top:4px}
.hero-text .l3{font-size:44px;font-weight:300;line-height:1.05}
.hero-text .more{font-size:12px;letter-spacing:3px;margin-top:18px;display:inline-block;border-bottom:1px solid #fff;padding-bottom:2px}

/* about */
.about{top:585px;height:472px;background:linear-gradient(180deg,#f4f5f7,#e9ebee)}
.about-decor{left:0;top:0;width:1200px;height:472px;background:radial-gradient(ellipse at 18% 50%,#e0e2e6 0,transparent 40%),radial-gradient(ellipse at 85% 45%,#e2e4e8 0,transparent 38%)}
.about-photo{left:280px;top:30px;width:280px;height:442px;background:linear-gradient(180deg,#d6dbe3 0%,#3a3f52 55%,#1f2433 100%)}
.about-copy{left:610px;top:92px;width:380px}
.about-title{font-size:40px;font-weight:700;color:var(--blue);line-height:1}
.about-title .boxed{border:2px solid var(--blue);padding:0 4px}
.about-sub{font-size:32px;font-weight:300;color:var(--ink);margin-top:10px;letter-spacing:.5px}
.about-lead{font-size:14px;color:var(--muted);margin-top:14px;line-height:1.5}
.about-body{font-size:10.5px;color:var(--muted);margin-top:12px;line-height:1.75}
.btn{display:inline-block;background:var(--blue);color:#fff;font-size:10px;font-weight:700;letter-spacing:.5px;text-align:center}
.about .btn{width:130px;height:38px;line-height:38px;margin-top:22px}

/* section headings */
.scale-icon{position:absolute;left:540px;width:120px;height:24px}
.scale-icon::before,.scale-icon::after{content:"";position:absolute;top:11px;width:40px;height:1px;background:currentColor;opacity:.6}
.scale-icon::before{left:0}.scale-icon::after{right:0}
.scale-icon svg{position:absolute;left:49px;top:0}
.sec-title{position:absolute;left:0;width:1200px;text-align:center;font-size:36px;font-weight:700;letter-spacing:1px}

/* services */
.services{top:1057px;height:576px;color:#fff}
.services-bg{position:absolute;inset:0;background:linear-gradient(180deg,#242a38 0%,#1c2230 60%,#282e3c 100%)}
.service{width:180px;text-align:center}
.service .ring{width:82px;height:82px;border:2px solid #fff;border-radius:50%;margin:0 auto;display:flex;align-items:center;justify-content:center}
.service h3{font-size:12.5px;font-weight:500;margin-top:24px}
.service p{font-size:9px;line-height:1.6;margin-top:8px;color:#d5d9e0}

/* practice */
.practice{top:1633px;height:625px;background:var(--white)}
.practice-decor{left:820px;top:0;width:380px;height:625px;background:linear-gradient(90deg,rgba(255,255,255,0),#eceef1 60%,#e3e5e8)}
.card{top:172px;width:271px;height:383px}
.card .pill{position:absolute;left:0;top:340px;background:#fff;border-radius:0 16px 16px 0;height:28px;line-height:28px;padding:0 14px 0 8px;font-size:11px;font-weight:700;color:var(--blue-deep)}

/* testimonials */
.testimonials{top:2258px;height:512px;background:var(--blue);color:#fff}
.testimonials-decor{left:0;top:0;width:1200px;height:512px;background:radial-gradient(ellipse at 70% 60%,rgba(255,255,255,.07),transparent 45%)}
.avatar{left:544px;top:152px;width:112px;height:112px;border-radius:50%;border:4px solid #fff;background:linear-gradient(180deg,#c9ced6,#7d8695)}
.t-name{top:280px;width:1200px;text-align:center;font-size:14px;font-weight:700}
.t-role{top:300px;width:1200px;text-align:center;font-size:11px;color:#d7e2f5}
.t-quote{left:300px;top:332px;width:600px;text-align:center;font-size:15.5px;line-height:1.6;color:#d7e2f5}
.t-mark{left:578px;top:398px}
.dots{left:586px;top:456px;display:flex;gap:10px}
.dots span{width:8px;height:8px;border-radius:50%;border:1px solid #fff}
.dots span.on{background:#fff}

/* clients */
.clients{top:2770px;height:342px;background:#fff}
.client{top:160px;width:164px;height:120px;border:1px solid #e0e2e6;display:flex;align-items:center;justify-content:center;gap:8px;font-size:16px;font-weight:700;color:var(--navy)}
.client i{width:14px;height:14px;background:var(--navy);display:block}
.arrow{top:205px}

/* footer */
.site-footer{top:3112px;height:356px;background:var(--footer);color:#fff}
.f-brand{left:166px;top:74px;width:140px;text-align:center;font-weight:500;color:#fff;line-height:1.15}
.f-about{left:176px;top:156px;width:220px;font-size:10.5px;line-height:1.6;color:#d0d0d0}
.f-h{font-size:13px;font-weight:700;letter-spacing:.5px}
.f-links{left:440px;top:58px}
.f-links ul{list-style:none;margin-top:30px}
.f-links li{font-size:11px;color:#ddd;margin-bottom:20px;display:flex;align-items:center;gap:8px}
.f-links li::before{content:"";border-left:5px solid #fff;border-top:4px solid transparent;border-bottom:4px solid transparent}
.f-info{left:590px;top:58px;width:190px}
.f-info dl{margin-top:28px;font-size:10.5px;color:#ddd;line-height:1.6}
.f-info dt{display:inline;font-weight:500}
.f-info dd{display:inline;margin-left:4px}
.f-info .row{margin-bottom:14px}
.f-contact{left:802px;top:58px;width:222px}
.field{background:#fff;color:#333;font-size:10px;padding:0 10px;height:34px;line-height:34px;margin-top:10px}
.field.first{margin-top:30px}
.field.msg{height:70px;line-height:26px}
.f-contact .btn{width:96px;height:30px;line-height:30px;margin-top:16px;background:var(--blue)}

.bottombar{top:3468px;height:61px;background:var(--blue);color:#dfe7f5}
.copy{left:176px;top:23px;font-size:9.5px;line-height:1.6}
.b-social{left:856px;top:18px;display:flex;gap:6px}
.b-social span{width:24px;height:24px;border-radius:50%;background:#fff;display:block}
</style>
</head>
<body>

<header class="topbar">
  <div class="brand abs">
    <div class="brand-name">CRESTMOOR</div>
    <div class="brand-sub">LAW</div>
  </div>
  <div class="contact-item abs" style="left:402px">
    <svg width="26" height="34" viewBox="0 0 26 34" fill="none" stroke="#222" stroke-width="1.6"><rect x="4" y="1" width="18" height="32" rx="3"/><line x1="10" y1="28" x2="16" y2="28"/></svg>
    <div><div class="big">+(123)-456 6789</div><div class="small">Call us Now!</div></div>
  </div>
  <div class="contact-item abs" style="left:585px">
    <svg width="34" height="24" viewBox="0 0 34 24" fill="none" stroke="#222" stroke-width="1.6"><rect x="1" y="1" width="32" height="22"/><polyline points="1,1 17,13 33,1"/></svg>
    <div><div class="big">info@crestmoorlaw.com</div><div class="small">Email Address</div></div>
  </div>
  <div class="socials abs" aria-label="Social profiles"><span></span><span></span><span></span><span></span></div>
</header>

<nav class="mainnav">
  <ul>
    <li class="current">Home</li><li>About us</li><li>Series</li><li>Areas of Practice</li><li>Testimonials</li><li>Blog</li><li>Contact Us</li>
  </ul>
  <div class="search abs">Search...
    <svg width="13" height="13" viewBox="0 0 13 13" fill="none" stroke="#fff" stroke-width="1.6"><circle cx="5.5" cy="5.5" r="4.3"/><line x1="8.7" y1="8.7" x2="12" y2="12"/></svg>
  </div>
</nav>

<section class="hero">
  <div class="hero-photo" role="img" aria-label="Group of lawyers in suits standing together, dark toned"></div>
  <div class="hero-frame abs"></div>
  <div class="hero-line abs"></div>
  <div class="hero-text abs">
    <div class="l1">BUSINESS LAW</div>
    <div class="l2">AND DISPUTE</div>
    <div class="l3">RESOLUTION</div>
    <div class="more">LEARN MORE</div>
  </div>
</section>

<section class="about">
  <div class="about-decor abs" role="img" aria-label="Faint scales of justice backdrop"></div>
  <div class="about-photo abs" role="img" aria-label="Portrait of the founding lawyer in a dark suit and red tie"></div>
  <div class="about-copy abs">
    <div class="about-title"><span class="boxed">ABOUT</span> US</div>
    <div class="about-sub">CRESTMOOR LAW</div>
    <p class="about-lead">Lorem Ipsum is simply dummy text of the printing and typesetting industry. Lorem Ipsum has been the industry's</p>
    <p class="about-body">Lorem Ipsum is simply dummy text of the printing and typesetting industry. Lorem Ipsum has been the industry's standard dummy text ever since the 1500s, when an unknown printer took a galley of type and scrambled it to make a type specimen book. It has survived not only five centuries, but also the leap into electronic typesetting, remaining essentially unchanged.</p>
    <span class="btn">READ MORE</span>
  </div>
</section>

<section class="services">
  <div class="services-bg" role="img" aria-label="Statue of Lady Justice with sword and scales on a dark background"></div>
  <div class="scale-icon" style="top:52px;color:#fff">
    <svg width="22" height="22" viewBox="0 0 22 22" fill="none" stroke="#fff" stroke-width="1.4"><line x1="11" y1="2" x2="11" y2="19"/><line x1="3" y1="5" x2="19" y2="5"/><path d="M1 12 L4 5 L7 12 Z"/><path d="M15 12 L18 5 L21 12 Z"/><line x1="6" y1="19" x2="16" y2="19"/></svg>
  </div>
  <h2 class="sec-title" style="top:86px;color:#fff">OUR SERVICES</h2>

  <div class="service abs" style="left:310px;top:169px">
    <div class="ring"><svg width="34" height="30" viewBox="0 0 34 30" fill="none" stroke="#fff" stroke-width="1.8"><rect x="2" y="8" width="30" height="20" rx="2"/><path d="M12 8 V4 H22 V8"/><line x1="2" y1="16" x2="32" y2="16"/></svg></div>
    <h3>Special Services</h3><p>Lorem Ipsum is simply dummy text of the printing and typesetting industry.</p>
  </div>
  <div class="service abs" style="left:510px;top:169px">
    <div class="ring"><svg width="38" height="32" viewBox="0 0 38 32" fill="none" stroke="#fff" stroke-width="1.8"><circle cx="12" cy="8" r="5"/><circle cx="26" cy="8" r="5"/><path d="M3 30 V20 Q12 13 21 20 V30"/><path d="M17 30 V20 Q26 13 35 20 V30"/></svg></div>
    <h3>Family Law</h3><p>Lorem Ipsum is simply dummy text of the printing and typesetting industry.</p>
  </div>
  <div class="service abs" style="left:710px;top:169px">
    <div class="ring"><svg width="34" height="34" viewBox="0 0 34 34" fill="none" stroke="#fff" stroke-width="1.8"><path d="M2 16 Q17 0 32 16 Z"/><path d="M17 16 V28 Q17 32 13 30"/></svg></div>
    <h3>Insurance Services</h3><p>Lorem Ipsum is simply dummy text of the printing and typesetting industry.</p>
  </div>
  <div class="service abs" style="left:310px;top:368px">
    <div class="ring"><svg width="34" height="34" viewBox="0 0 34 34" fill="none" stroke="#fff" stroke-width="1.8"><polygon points="17,2 21.5,12.5 32,13 24,20.5 26.5,31 17,25.5 7.5,31 10,20.5 2,13 12.5,12.5"/></svg></div>
    <h3>Drug Offences</h3><p>Lorem Ipsum is simply dummy text of the printing and typesetting industry.</p>
  </div>
  <div class="service abs" style="left:510px;top:368px">
    <div class="ring"><svg width="28" height="36" viewBox="0 0 28 36" fill="none" stroke="#fff" stroke-width="1.8"><path d="M14 2 Q26 14 24 24 Q22 34 14 34 Q4 34 4 24 Q4 16 10 10 Q10 18 14 18 Q18 12 14 2 Z"/></svg></div>
    <h3>Fire Accident</h3><p>Lorem Ipsum is simply dummy text of the printing and typesetting industry.</p>
  </div>
  <div class="service abs" style="left:710px;top:368px">
    <div class="ring"><svg width="34" height="32" viewBox="0 0 34 32" fill="none" stroke="#fff" stroke-width="1.8"><rect x="2" y="2" width="30" height="28"/><rect x="7" y="20" width="4" height="6"/><rect x="14" y="15" width="4" height="11"/><rect x="21" y="10" width="4" height="16"/><polyline points="6,14 14,8 20,10 28,5"/></svg></div>
    <h3>Immigration</h3><p>Lorem Ipsum is simply dummy text of the printing and typesetting industry.</p>
  </div>
</section>

<section class="practice">
  <div class="practice-decor abs" role="img" aria-label="Faded portrait of a smiling businessman"></div>
  <div class="scale-icon" style="top:48px;color:#333">
    <svg width="22" height="22" viewBox="0 0 22 22" fill="none" stroke="#333" stroke-width="1.4"><line x1="11" y1="2" x2="11" y2="19"/><line x1="3" y1="5" x2="19" y2="5"/><path d="M1 12 L4 5 L7 12 Z"/><path d="M15 12 L18 5 L21 12 Z"/><line x1="6" y1="19" x2="16" y2="19"/></svg>
  </div>
  <h2 class="sec-title" style="top:88px;color:var(--blue)">PRACTICE AREAS</h2>

  <div class="card abs" style="left:176px">
    <div class="abs" style="inset:0;background:linear-gradient(160deg,#f3e2b8 0%,#c8a46a 45%,#3c2a1a 100%)" role="img" aria-label="Judge's gavel resting on an open law book"></div>
    <span class="pill">Corporate Transactions and Regulation</span>
  </div>
  <div class="card abs" style="left:464px">
    <div class="abs" style="inset:0;background:linear-gradient(180deg,#7a5a3a 0%,#3a3e4c 50%,#22263a 100%)" role="img" aria-label="Young lawyer reading a book in a library"></div>
    <span class="pill">Corporate Transactions and Regulation</span>
  </div>
  <div class="card abs" style="left:752px">
    <div class="abs" style="inset:0;background:linear-gradient(150deg,#5a4026 0%,#8a6a48 45%,#2c2420 100%)" role="img" aria-label="Lawyer signing documents at a desk"></div>
    <span class="pill">Corporate Transactions and Regulation</span>
  </div>
</section>

<section class="testimonials">
  <div class="testimonials-decor abs" role="img" aria-label="Faint gavel backdrop in blue"></div>
  <div class="scale-icon" style="top:50px;color:#fff">
    <svg width="22" height="22" viewBox="0 0 22 22" fill="none" stroke="#fff" stroke-width="1.4"><line x1="11" y1="2" x2="11" y2="19"/><line x1="3" y1="5" x2="19" y2="5"/><path d="M1 12 L4 5 L7 12 Z"/><path d="M15 12 L18 5 L21 12 Z"/><line x1="6" y1="19" x2="16" y2="19"/></svg>
  </div>
  <h2 class="sec-title" style="top:86px;color:#fff">TESTIMONIALS</h2>
  <div class="avatar abs" role="img" aria-label="Client portrait"></div>
  <div class="t-name abs">JOHN DOE</div>
  <div class="t-role abs">Owner &amp; Founder</div>
  <p class="t-quote abs">Lorem Ipsum is simply dummy text of the printing and typesetting industry. Lorem Ipsum has been the industry's standard dummy text ever since the 1500s,</p>
  <svg class="t-mark abs" width="44" height="36" viewBox="0 0 44 36" fill="#fff"><path d="M2 2 H18 V18 L12 34 H4 L9 18 H2 Z"/><path d="M24 2 H40 V18 L34 34 H26 L31 18 H24 Z"/></svg>
  <div class="dots abs"><span class="on"></span><span></span></div>
</section>

<section class="clients">
  <div class="scale-icon" style="top:48px;color:#333">
    <svg width="22" height="22" viewBox="0 0 22 22" fill="none" stroke="#333" stroke-width="1.4"><line x1="11" y1="2" x2="11" y2="19"/><line x1="3" y1="5" x2="19" y2="5"/><path d="M1 12 L4 5 L7 12 Z"/><path d="M15 12 L18 5 L21 12 Z"/><line x1="6" y1="19" x2="16" y2="19"/></svg>
  </div>
  <h2 class="sec-title" style="top:92px;color:var(--blue)">OUR CLIENTS</h2>
  <svg class="arrow abs" style="left:120px" width="24" height="30" viewBox="0 0 24 30" fill="none" stroke="#0a4ea8" stroke-width="4"><polyline points="18,3 6,15 18,27"/></svg>
  <div class="client abs" style="left:176px"><i></i>Brennan Law</div>
  <div class="client abs" style="left:346px"><i></i>Orbit Legal Aid</div>
  <div class="client abs" style="left:518px">Tolland Law</div>
  <div class="client abs" style="left:690px"><i></i>Ashgrove Law</div>
  <div class="client abs" style="left:860px">Pembury Law</div>
  <svg class="arrow abs" style="left:1054px" width="24" height="30" viewBox="0 0 24 30" fill="none" stroke="#0a4ea8" stroke-width="4"><polyline points="6,3 18,15 6,27"/></svg>
</section>

<footer class="site-footer">
  <div class="f-brand abs">
    <div class="brand-name">CRESTMOOR</div>
    <div class="brand-sub">LAW</div>
  </div>
  <p class="f-about abs">Lorem Ipsum is simply dummy text of the printing and typesetting industry. Lorem Ipsum has been the industry's standard dummy text ever since the 1500s, when an unknown printer took a galley of type and scrambled it to make a type specimen book. It has survived not only five centuries.</p>
  <div class="f-links abs">
    <div class="f-h">QUIK LINK</div>
    <ul><li>Home</li><li>Services</li><li>Practice Area</li><li>Testimonials</li><li>Blog</li></ul>
  </div>
  <div class="f-info abs">
    <div class="f-h">INFORMATION</div>
    <dl>
      <div class="row"><dt>OFFICE:</dt><dd>Lorem Ipsum is simply dummy text of the printing and typesetting industry</dd></div>
      <div class="row"><dt>PHONE:</dt><dd>(123) 456-6789</dd></div>
      <div class="row"><dt>FAX:</dt><dd>(123) 456-6789</dd></div>
      <div class="row"><dt>EMAIL:</dt><dd>info@crestmoorlaw.com</dd></div>
    </dl>
  </div>
  <div class="f-contact abs">
    <div class="f-h">CONTACT US</div>
    <div class="field first">Name</div>
    <div class="field">Email</div>
    <div class="field msg">Messages</div>
    <span class="btn">SEND</span>
  </div>
</footer>

<div class="bottombar abs" style="left:0;width:1200px">
  <p class="copy abs">Copyright © 2019 <b>Crestmoor Law</b> All Rights Reserved.</p>
  <div class="b-social abs" aria-label="Social profiles"><span></span><span></span><span></span><span></span><span></span><span></span></div>
</div>

</body>
</html>
```